Design a New Business Card for Our Company

We are looking for fresh, unique, and a modern business card that reflects our roots as digital marketing agency focused on SEM.

Industry/Entity Type

Marketing

Contact Information for Business Card

looking for very unique out of the box designs. clean and modern that compliments our logo

Requirements
Must have
• colors should match our logo
• Front should have name, address, email, and phone/fax of the person, phone/fax are the same number
• back should have our url

```html
<!DOCTYPE html>
<html lang="en">
<head>
<meta charset="utf-8">
<title>Brightwave Media — Business Card</title>
<link href="https://fonts.googleapis.com/css2?family=Arimo:wght@400;700&display=swap" rel="stylesheet">
<style>
  :root {
    --page-bg: #2b2b2d;
    --card-navy: #0f3056;
    --card-navy-deep: #0b2646;
    --card-navy-soft: #1a4170;
    --accent-blue: #7eb4e6;
    --text-grey: #c9ccd1;
    --divider: #5d7b9d;
  }
  * { box-sizing: border-box; margin: 0; padding: 0; }
  html, body {
    width: 1200px; height: 960px; overflow: hidden;
    background: var(--page-bg);
    font-family: "Arimo", Arial, sans-serif;
  }
  .sheet {
    width: 1200px; height: 960px;
    display: flex; flex-direction: column; align-items: center; justify-content: center;
    gap: 40px;
  }
  .card {
    position: relative;
    width: 700px; height: 400px;
    border-radius: 26px;
    overflow: hidden;
    background: linear-gradient(160deg, var(--card-navy) 0%, var(--card-navy-deep) 100%);
    box-shadow: 0 10px 30px rgba(0,0,0,.45);
  }
  .card-texture {
    position: absolute; inset: 0;
    background: radial-gradient(ellipse at 80% 15%, var(--card-navy-soft) 0%, transparent 60%);
    opacity: .7;
  }
  .brand {
    position: absolute;
    display: flex; align-items: center; gap: 16px;
    font-weight: 700; color: var(--text-grey);
    letter-spacing: -1px;
    white-space: nowrap;
  }
  .brand-dot { border-radius: 50%; background: var(--accent-blue); flex: none; }

  /* front */
  .front .brand { left: 50px; top: 100px; font-size: 44px; }
  .front .brand-dot { width: 40px; height: 40px; }
  .person { position: absolute; left: 64px; top: 252px; }
  .person-name { font-size: 24px; font-weight: 700; color: var(--accent-blue); }
  .person-title { font-size: 15px; color: var(--text-grey); margin-top: 2px; }
  .person-web { font-size: 15px; color: var(--text-grey); margin-top: 24px; }
  .contact {
    position: absolute; left: 398px; top: 236px;
    border-left: 1px solid var(--divider);
    padding-left: 12px; height: 110px;
    font-size: 15px; color: var(--text-grey); line-height: 1.25;
    white-space: nowrap;
  }
  .contact-address { margin-bottom: 18px; }
  .contact-label { color: var(--accent-blue); font-weight: 700; display: inline-block; width: 16px; }
  .contact-email { font-weight: 700; }

  /* back */
  .back .brand { left: 80px; top: 140px; font-size: 52px; }
  .back .brand-dot { width: 72px; height: 72px; }
  .back-web {
    position: absolute; left: 170px; top: 230px;
    font-size: 16px; color: var(--accent-blue);
    white-space: nowrap;
  }
</style>
</head>
<body>
<main class="sheet">
  <section class="card front" aria-label="Card front">
    <div class="card-texture" role="img" aria-label="Faint soft circles scattered across the navy background"></div>
    <div class="brand"><span class="brand-dot"></span><span>Brightwave Media</span></div>
    <div class="person">
      <p class="person-name">Daniel Reyes</p>
      <p class="person-title">Sales Manager</p>
      <p class="person-web">www.brightwavemedia.com</p>
    </div>
    <div class="contact">
      <p class="contact-address">1480 Maple Ridge Rd Fairview,<br>CA 90210 USA</p>
      <p><span class="contact-label">P</span>: 555.014.2290</p>
      <p><span class="contact-label">F</span>: 555.014.2290</p>
      <p><span class="contact-label">E</span>: <span class="contact-email">daniel@brightwavemedia.com</span></p>
    </div>
  </section>

  <section class="card back" aria-label="Card back">
    <div class="card-texture" role="img" aria-label="Faint pattern of small web and social icons over the navy background"></div>
    <div class="brand"><span class="brand-dot"></span><span>Brightwave Media</span></div>
    <p class="back-web">www.brightwavemedia.com</p>
  </section>
</main>
</body>
</html>
```